Pediatric Dentist Business Card

I need a business card designed for a dentist who works exclusively with children.
We prefer designs that are out of ordiary that is fun and interesting to kids.

there is no logo since this is a dentists office. The name of the doctor is "Tavor Kesh" if you want to get creative with that.

Target Market(s)

Kids

Industry/Entity Type

Business

Contact Information for Business Card

Anythings that is creative

Colors

Designer to choose colors to be used in the design.

```html
<!DOCTYPE html>
<html lang="en">
<head>
<meta charset="utf-8">
<title>Tavor Kesh – Pediatric Dentist Business Card</title>
<link rel="stylesheet" href="https://fonts.googleapis.com/css2?family=Open+Sans:wght@400;600;700&display=swap">
<style>
  :root {
    --bg: #dcdcdc;
    --paper: #ffffff;
    --pink: #f5a6f5;
    --yellow: #ffd400;
    --olive: #9a7a0a;
    --ink: #1c1c1c;
  }
  html, body {
    margin: 0;
    width: 1200px;
    height: 1200px;
    overflow: hidden;
    background: var(--bg);
    font-family: "Open Sans", sans-serif;
  }
  .canvas {
    position: relative;
    width: 1200px;
    height: 1200px;
  }
  .card {
    position: absolute;
    left: 150px;
    width: 900px;
    height: 514px;
    background: var(--paper);
    box-shadow: 0 10px 28px rgba(0,0,0,0.18);
    overflow: hidden;
  }
  .card--front { top: 50px; }
  .card--back { top: 636px; }
  .card svg.art {
    position: absolute;
    inset: 0;
    width: 100%;
    height: 100%;
  }
  /* front */
  .brand {
    position: absolute;
    left: 300px;
    top: 200px;
    display: flex;
    align-items: center;
    gap: 16px;
  }
  .brand__mark {
    width: 44px;
    height: 44px;
    border-radius: 50%;
    background: var(--yellow);
  }
  .brand__name {
    font-size: 56px;
    font-weight: 700;
    color: var(--olive);
    letter-spacing: 0.5px;
  }
  .front__web {
    position: absolute;
    left: 530px;
    top: 330px;
    font-size: 17px;
    color: var(--ink);
    transform: rotate(-14deg);
    transform-origin: left center;
  }
  /* back */
  .identity {
    position: absolute;
    left: 60px;
    top: 170px;
  }
  .identity__name {
    margin: 0;
    font-size: 40px;
    font-weight: 400;
    color: var(--ink);
    letter-spacing: 1px;
  }
  .identity__role {
    margin: 4px 0 0;
    font-size: 26px;
    font-weight: 600;
    color: var(--olive);
    letter-spacing: 2px;
  }
  .mascot {
    position: absolute;
    left: 150px;
    top: 285px;
    width: 150px;
    height: 110px;
    border-radius: 40px 40px 30px 30px;
    background: linear-gradient(90deg, var(--pink), var(--yellow));
  }
  .contacts {
    position: absolute;
    right: 50px;
    top: 40px;
    margin: 0;
    padding: 0;
    list-style: none;
  }
  .contacts li {
    display: flex;
    justify-content: flex-end;
    align-items: center;
    gap: 16px;
    height: 52px;
    font-size: 18px;
    color: #ffffff;
  }
  .contacts .icon {
    width: 40px;
    height: 34px;
    border: 2px solid var(--pink);
    box-sizing: border-box;
    display: flex;
    align-items: center;
    justify-content: center;
  }
  .contacts .icon svg { width: 22px; height: 22px; }
</style>
</head>
<body>
<main class="canvas">

  <section class="card card--front" aria-label="Card front">
    <svg class="art" viewBox="0 0 900 514" preserveAspectRatio="none" aria-hidden="true">
      <path d="M0 0 H900 V10 C640 80 300 150 0 220 Z" fill="var(--pink)"/>
      <path d="M0 250 C320 170 650 110 900 30" fill="none" stroke="var(--yellow)" stroke-width="6"/>
      <path d="M0 480 C300 380 600 300 900 240" fill="none" stroke="var(--pink)" stroke-width="8"/>
      <path d="M40 514 C320 420 620 330 900 270 V514 Z" fill="var(--yellow)"/>
      <g fill="#ffffff">
        <circle cx="250" cy="430" r="3"/>
        <circle cx="290" cy="420" r="4"/>
        <circle cx="330" cy="410" r="5"/>
        <circle cx="370" cy="399" r="6"/>
        <circle cx="410" cy="388" r="7"/>
        <circle cx="450" cy="377" r="8"/>
        <circle cx="700" cy="310" r="8"/>
        <circle cx="740" cy="300" r="7"/>
        <circle cx="780" cy="291" r="6"/>
        <circle cx="820" cy="282" r="4"/>
        <circle cx="860" cy="274" r="3"/>
      </g>
    </svg>
    <div class="brand">
      <span class="brand__mark"></span>
      <span class="brand__name">Tavor Kesh</span>
    </div>
    <div class="front__web">www.tavorkeshsmiles.com</div>
  </section>

  <section class="card card--back" aria-label="Card back">
    <svg class="art" viewBox="0 0 900 514" preserveAspectRatio="none" aria-hidden="true">
      <path d="M250 0 H900 V260 C800 290 720 310 650 330 Z" fill="var(--olive)"/>
      <path d="M120 514 C380 360 640 270 900 225 V514 Z" fill="var(--yellow)"/>
      <path d="M90 514 C360 350 620 265 900 210" fill="none" stroke="var(--yellow)" stroke-width="7"/>
      <path d="M610 345 C720 300 820 270 900 255" fill="none" stroke="var(--olive)" stroke-width="6"/>
    </svg>

    <div class="identity">
      <h1 class="identity__name">TAVOR KESH</h1>
      <p class="identity__role">Pediatric Dentist</p>
    </div>
    <div class="mascot" role="img" aria-label="Illustration of two smiling cartoon teeth, pink and yellow"></div>

    <ul class="contacts">
      <li>your city address
        <span class="icon"><svg viewBox="0 0 24 24"><path d="M3 12 L12 4 L21 12 V20 H3 Z" fill="var(--pink)"/></svg></span>
      </li>
      <li>hello@tavorkeshsmiles.com
        <span class="icon"><svg viewBox="0 0 24 24"><rect x="2" y="5" width="20" height="14" fill="var(--pink)"/><path d="M2 5 L12 13 L22 5" fill="none" stroke="#ffffff" stroke-width="1.5"/></svg></span>
      </li>
      <li>1234-5678-91011
        <span class="icon"><svg viewBox="0 0 24 24"><rect x="7" y="2" width="10" height="20" rx="2" fill="none" stroke="var(--pink)" stroke-width="2"/><circle cx="12" cy="18" r="1.3" fill="var(--pink)"/></svg></span>
      </li>
      <li>www.tavorkeshsmiles.com
        <span class="icon"><svg viewBox="0 0 24 24" fill="none" stroke="var(--pink)" stroke-width="1.6"><circle cx="12" cy="12" r="9"/><ellipse cx="12" cy="12" rx="4" ry="9"/><path d="M3 12 H21 M5 7 H19 M5 17 H19"/></svg></span>
      </li>
    </ul>
  </section>

</main>
</body>
</html>
```